Elegant stationary design with logo

Looking for a simple elegant design incorporating the logo with similar colors. Will be used for PDFs and invoice templates. Rose gold, blush pink, copper hues are the colors. Final product to be able to be used as a template for word documents, PDFs, invoice, and training materials.

Target Market(s)

Small business owners mostly females.

Font styles to use
Serif
Script

Colors
feeeee
fee3d5

Requirements
Must have
• Colors and incorporate logo.
Nice to have
• Simple design with elegant edging.
Should not have
• Nothing too busy or techy.

```html
<!DOCTYPE html>
<html lang="en">
<head>
<meta charset="utf-8">
<title>Willow Bloom Studio — Stationery</title>
<link rel="stylesheet" href="https://fonts.googleapis.com/css2?family=Cormorant+Garamond:wght@400&family=Lato:wght@400&display=swap">
<style>
  :root {
    --backdrop: #ece8e6;
    --paper: #ffffff;
    --copper: #e3a27f;
    --blush: #d9b1ab;
    --rule: #dcaea6;
    --ink: #3a3a3a;
    --card-edge: #b5b5b5;
  }
  * { box-sizing: border-box; margin: 0; padding: 0; }
  html, body { width: 900px; height: 1200px; overflow: hidden; }
  body { background: var(--backdrop); position: relative; font-family: "Lato", sans-serif; color: var(--ink); }

  .letterhead {
    position: absolute; left: 57px; top: 85px; width: 788px; height: 1025px;
    background: var(--paper); box-shadow: 0 2px 6px rgba(0,0,0,.12);
  }
  .business-card {
    position: absolute; left: 333px; top: 650px; width: 548px; height: 327px;
    background: var(--paper); border: 3px solid var(--card-edge); border-radius: 22px;
  }

  .brand { position: absolute; text-align: center; }
  .brand-dot { display: block; margin: 0 auto; border-radius: 50%; border: 2px solid var(--copper); }
  .brand-name {
    font-family: "Cormorant Garamond", serif; font-weight: 400; color: var(--blush);
    text-transform: uppercase; letter-spacing: .04em; line-height: 1.05;
  }

  .divider { position: absolute; width: 2px; background: var(--rule); }

  .contact-list { position: absolute; list-style: none; }
  .contact-list li { display: flex; align-items: center; }
  .contact-icon { flex: none; }
  .contact-icon rect.copper { fill: var(--copper); }
  .contact-icon rect.blush { fill: var(--blush); }
  .contact-icon .glyph { fill: none; stroke: #fff; stroke-width: 1.6; stroke-linecap: round; stroke-linejoin: round; }

  /* letterhead sizes */
  .letterhead .brand { left: 58px; top: 62px; width: 160px; }
  .letterhead .brand-dot { width: 70px; height: 70px; margin-bottom: 8px; }
  .letterhead .brand-name { font-size: 24px; }
  .letterhead .divider { left: 393px; top: 58px; height: 116px; }
  .letterhead .contact-list { left: 528px; top: 67px; font-size: 17px; }
  .letterhead .contact-list li { height: 26px; }
  .letterhead .contact-icon { width: 22px; height: 22px; margin-right: 10px; }

  /* card sizes */
  .business-card .brand { left: 40px; top: 122px; width: 136px; }
  .business-card .brand-dot { width: 58px; height: 58px; margin-bottom: 6px; }
  .business-card .brand-name { font-size: 20px; }
  .business-card .divider { left: 273px; top: 124px; height: 90px; }
  .business-card .contact-list { left: 345px; top: 127px; font-size: 13px; }
  .business-card .contact-list li { height: 21px; }
  .business-card .contact-icon { width: 18px; height: 18px; margin-right: 8px; }
</style>
</head>
<body>

<svg width="0" height="0" style="position:absolute">
  <defs>
    <symbol id="icon-mobile" viewBox="0 0 22 22"><rect x="7" y="4" width="8" height="14" rx="1.5" class="glyph"/></symbol>
    <symbol id="icon-phone" viewBox="0 0 22 22"><path class="glyph" d="M6 5c0 6 5 11 11 12l1-3-3-1-2 1c-2-1-4-3-5-5l1-2-1-3z"/></symbol>
    <symbol id="icon-globe" viewBox="0 0 22 22"><circle cx="11" cy="11" r="6" class="glyph"/><path class="glyph" d="M5 11h12M11 5c-3 3-3 9 0 12M11 5c3 3 3 9 0 12"/></symbol>
    <symbol id="icon-mail" viewBox="0 0 22 22"><rect x="4" y="6" width="14" height="10" class="glyph"/><path class="glyph" d="M4 6l7 6 7-6"/></symbol>
  </defs>
</svg>

<section class="letterhead">
  <div class="brand">
    <span class="brand-dot"></span>
    <p class="brand-name">Willow Bloom<br>Studio</p>
  </div>
  <div class="divider"></div>
  <ul class="contact-list">
    <li><svg class="contact-icon" viewBox="0 0 22 22"><rect class="copper" width="22" height="22"/><use href="#icon-mobile"/></svg>+ 011 11111111</li>
    <li><svg class="contact-icon" viewBox="0 0 22 22"><rect class="blush" width="22" height="22"/><use href="#icon-phone"/></svg>+ 011 11111111</li>
    <li><svg class="contact-icon" viewBox="0 0 22 22"><rect class="copper" width="22" height="22"/><use href="#icon-globe"/></svg>www.wbstudio.com</li>
    <li><svg class="contact-icon" viewBox="0 0 22 22"><rect class="blush" width="22" height="22"/><use href="#icon-mail"/></svg>xxx@wbstudio.com</li>
  </ul>
</section>

<section class="business-card">
  <div class="brand">
    <span class="brand-dot"></span>
    <p class="brand-name">Willow Bloom<br>Studio</p>
  </div>
  <div class="divider"></div>
  <ul class="contact-list">
    <li><svg class="contact-icon" viewBox="0 0 22 22"><rect class="copper" width="22" height="22"/><use href="#icon-mobile"/></svg>+ 011 11111111</li>
    <li><svg class="contact-icon" viewBox="0 0 22 22"><rect class="blush" width="22" height="22"/><use href="#icon-phone"/></svg>+ 011 11111111</li>
    <li><svg class="contact-icon" viewBox="0 0 22 22"><rect class="copper" width="22" height="22"/><use href="#icon-globe"/></svg>www.wbstudio.com</li>
    <li><svg class="contact-icon" viewBox="0 0 22 22"><rect class="blush" width="22" height="22"/><use href="#icon-mail"/></svg>xxx@wbstudio.com</li>
  </ul>
</section>

</body>
</html>
```